PRVD Traditional Business Card Project

Please see attached....just a simple business card... on attachment- please use the exact font, style, etc as the attached "Pat Everard Wynne" card... however, replace with the "Owen Reginald Talbot" text and address below the card.

```html
<!DOCTYPE html>
<html lang="en">
<head>
<meta charset="utf-8">
<title>PRVD Business Card</title>
<link rel="stylesheet" href="https://fonts.googleapis.com/css2?family=Tinos:wght@700&family=Michroma&family=Montserrat:wght@500&display=swap">
<style>
  :root {
    --stage: #000000;
    --card-dark: #2f2e2f;
    --card-light: #ffffff;
    --ink-light: #f2f2f2;
    --ink-dark: #111111;
  }
  * { margin: 0; padding: 0; box-sizing: border-box; }
  html, body {
    width: 1200px; height: 900px; overflow: hidden;
    background: var(--stage);
  }
  .stage { position: relative; width: 1200px; height: 900px; }
  .card { position: absolute; left: 302px; width: 560px; height: 344px; }
  .card--front { top: 126px; background: var(--card-dark); color: var(--ink-light); }
  .card--back { top: 492px; background: var(--card-light); color: var(--ink-dark); }

  .firm-mark {
    font-family: "Montserrat", "Arial", sans-serif;
    font-weight: 500; text-transform: uppercase;
  }
  .card--front .firm-mark {
    position: absolute; left: 30px; top: 36px; width: 260px;
    font-size: 15px; line-height: 21px; letter-spacing: 1px;
  }
  .card--back .firm-mark {
    position: absolute; left: 0; right: 0; top: 138px; text-align: center;
    font-size: 22px; line-height: 32px; letter-spacing: 1.5px;
  }

  .person { position: absolute; left: 0; right: 0; top: 134px; text-align: center; }
  .person-name {
    font-family: "Tinos", "Times New Roman", serif;
    font-weight: 700; font-variant: small-caps; white-space: nowrap;
    font-size: 33px; line-height: 36px; letter-spacing: 0.5px;
  }
  .title {
    font-family: "Michroma", "Arial", sans-serif; text-transform: uppercase; white-space: nowrap;
    font-size: 12.5px; letter-spacing: 3.5px; line-height: 22px;
  }

  .contact {
    position: absolute; top: 253px;
    font-family: "Montserrat", "Arial", sans-serif; font-weight: 500;
    font-size: 13.5px; line-height: 20px; white-space: nowrap;
  }
  .contact--address { left: 29px; }
  .contact--address .web { font-size: 14.5px; }
  .contact--lines { right: 28px; text-align: right; font-size: 15px; }
  .contact--lines .email { font-size: 14.5px; }
</style>
</head>
<body>
<main class="stage">
  <section class="card card--front">
    <div class="firm-mark">Pacific Ridge Valley Defense Group</div>
    <div class="person">
      <div class="person-name">Owen Reginald Talbot</div>
      <div class="title">Attorney at Law</div>
    </div>
    <div class="contact contact--address">
      <div>2140 CEDAR LANE, SUITE B</div>
      <div>OAKDALE HILLS, CA 90210</div>
      <div class="web">www.lawprvd.com</div>
    </div>
    <div class="contact contact--lines">
      <div>TEL:(555) 214-7700</div>
      <div>FAX:(555) 214-7701</div>
      <div class="email">otalbot@lawprvd.com</div>
    </div>
  </section>
  <section class="card card--back">
    <div class="firm-mark">Pacific Ridge Valley<br>Defense Group</div>
  </section>
</main>
</body>
</html>
```